Flyer/Broschürre für Ambulanter Betreuungsdienst
Zielgruppe
Ambulanter Betreuungsdienst,Dienstleistungen für Senioren und Menschen mit Beeinträchtigung
Nach Paragraph 43b 45a/b & 53b SGBXI
Unterstützung im Alltag:
-Begleitung zu Arztbesuchen,Therapien &Terminbegleitung aller Art,
-Hilfe beim Einkaufen & Besorgungen + Transport
-Unterstützung bei der Tagesstrukturierung & Organisation im Alltag
-Erinnerungsservice zb. Einahme von Medikamenten ggbf. Kontrolle
-Begleitung zu Sportveranstaltungen,Theater uvm.
für zuverlässige Sicherheit und Orientierung.
-Gemeinsames Spazieren gehen ( Bewegungsangebote)
- Lesen & Vorlesen
-Gemeinsames Kochen und geselschaft leisten beim essen.
-Unterstützung bei Terminplanungen,Hilfe bei der komunikation mit Medizinischen Personal.
Soziale Betreuung & Aktivierung:
-Geselschaft leisten,Gespräche führen ;
-Freizeitaktivitäten Planen & Durchführen
-Gemeinsames Lesen und Vorlesen
-Karten & Brettspiele spielen
-Malen & Basteln
-Briefe schreiben,Emails verfassen
-Gemeinsam alte interessen wecken und neue finden.
-Angehörige entlasten
-kommunikation & Informationsaustausch über Fortschritte und Bedürfnisse
-Betreuung & Aktivierung für Menschen mit Demenz
-Erinnerungspflege,Biografie Arbeit
-Individuelle Betreuung
-Kurz und Langzeit Betreuung
-Nachtpflege
-Bewegungsangebote
-Spiele spielen zb. Brett & Gemeinschsftsspiele
Dienstleistungen Haushaltsbereich
-Reinigung von Böden(Saugen & Wischen)
-Reinigung Küche und Bad
-Bett frisch Beziehen
-Fenster Reinigung (innen & außen)
-Haustiere versorgen (mit dem Hund spazieren gehen)
-Wäsche waschen
-Dekorieren
-uvm
Aufgabenstellung
Freundliches Design , vertrauenswürdiges Erscheinungsbild mit warmen Farben.
Firmenname ( Sonnwerk) logo sollte einen Sonnwerk darstellen.
Slogan Text:
Verlässlichkeit und Fürsorge mit Herz & Verstand.
Format soll handlich und nicht zu klein sein,damit Senioren es gut lesen bzw erkennen können.

```html
<!DOCTYPE html>
<html lang="de">
<head>
<meta charset="UTF-8">
<title>Sonnwerk – Ambulanter Betreuungsdienst</title>
<link href="https://fonts.googleapis.com/css2?family=Fira+Sans:wght@400;500;600&family=Fira+Sans+Condensed:wght@600&family=Caveat:wght@600&display=swap" rel="stylesheet">
<style>
  :root {
    --frame: #e5c9a1;
    --paper: #f7f2e3;
    --sage: #a9bf9e;
    --navy: #1f2a4a;
    --green-text: #2f5a3a;
    --divider: #9cb0c6;
    --gold: #d9a64a;
    --sage-icon: #8fb79a;
    --slate-icon: #7f9cbc;
    --band-blue: #a9c0d3;
  }
  * { margin: 0; padding: 0; box-sizing: border-box; }
  html, body { width: 1200px; height: 1200px; overflow: hidden; background: var(--frame); }
  .flyer { position: relative; width: 1200px; height: 1200px; background: var(--frame); font-family: "Fira Sans", sans-serif; color: var(--navy); }
  .sheet { position: absolute; left: 61px; top: 52px; width: 1078px; height: 1096px; background: var(--paper); }
  .brand-band { position: absolute; left: 61px; top: 114px; width: 1078px; height: 178px; background: var(--sage); }
  .brand-name { position: absolute; left: 0; width: 1184px; top: 132px; text-align: center; font-weight: 600; font-size: 76px; letter-spacing: 3px; color: var(--navy); }
  .brand-tagline { position: absolute; left: 0; width: 1184px; top: 232px; text-align: center; font-size: 30px; color: var(--green-text); letter-spacing: 0.5px; }
  .mascot { position: absolute; left: 858px; top: 78px; width: 262px; height: 240px; border-radius: 55% 45% 50% 50% / 50% 50% 50% 50%; background: radial-gradient(ellipse at 40% 50%, #e8b48c 0%, #d4ae8e 40%, #9aa4b2 75%, rgba(154,164,178,0) 100%); opacity: 0.8; }
  .slogan { position: absolute; left: 0; width: 1200px; top: 328px; text-align: center; font-family: "Caveat", cursive; font-weight: 600; font-size: 38px; color: var(--navy); }
  .divider { position: absolute; top: 418px; width: 3px; height: 314px; background: var(--divider); }
  .service { position: absolute; top: 445px; width: 330px; text-align: center; }
  .service svg { display: block; margin: 0 auto; height: 72px; }
  .service-title { margin-top: 26px; font-family: "Fira Sans Condensed", sans-serif; font-weight: 600; font-size: 29px; line-height: 36px; color: var(--navy); }
  .service-text { margin-top: 14px; font-size: 20px; line-height: 28px; color: var(--green-text); }
  .service-home .service-text { margin-top: 28px; }
  .photo { position: absolute; top: 758px; height: 217px; }
  .photo-friends { left: 105px; width: 304px; background: linear-gradient(135deg, #e9e6df, #c9c3b5 60%, #a9b7cc); }
  .photo-groceries { left: 452px; width: 296px; background: linear-gradient(135deg, #dfe3d6, #c8b9a2 55%, #94a88a); }
  .photo-plants { left: 793px; width: 304px; background: linear-gradient(135deg, #eceeee, #cfd5d3 55%, #8fa886); }
  .legal-band { position: absolute; left: 102px; top: 993px; width: 996px; height: 52px; background: var(--band-blue); display: flex; align-items: center; justify-content: center; font-size: 24px; color: var(--navy); }
  .contact { position: absolute; left: 0; width: 1200px; text-align: center; font-size: 22px; color: var(--green-text); }
  .contact-line1 { top: 1060px; }
  .contact-line2 { top: 1090px; }
  .contact span + span { margin-left: 12px; }
</style>
</head>
<body>
<div class="flyer">
  <div class="sheet"></div>
  <div class="brand-band"></div>
  <div class="brand-name">SONNWERK</div>
  <div class="brand-tagline">Ambulanter Betreuungsdienst</div>
  <div class="mascot" role="img" aria-label="Illustration eines Singvogels auf einem Zweig"></div>

  <p class="slogan">Verlässlichkeit und Fürsorge mit Herz &amp; Verstand.</p>

  <div class="divider" style="left:427px"></div>
  <div class="divider" style="left:770px"></div>

  <section class="service service-daily" style="left:92px">
    <svg viewBox="0 0 80 72" aria-hidden="true">
      <circle cx="32" cy="38" r="24" fill="none" stroke="var(--gold)" stroke-width="5"/>
      <path d="M32 24 V38 H42" fill="none" stroke="var(--gold)" stroke-width="4" stroke-linecap="round"/>
      <path d="M12 16 L20 8 M52 16 L44 8" stroke="var(--gold)" stroke-width="5" stroke-linecap="round"/>
      <rect x="48" y="42" width="26" height="26" rx="3" fill="var(--gold)"/>
      <path d="M54 44 V38 a7 7 0 0 1 14 0 V44" fill="none" stroke="var(--gold)" stroke-width="3"/>
    </svg>
    <h2 class="service-title">ALLTAGSBEGLEITUNG</h2>
    <p class="service-text">Unterstützung bei Terminen,<br>Einkauf &amp; Organisation.</p>
  </section>

  <section class="service service-social" style="left:434px">
    <svg viewBox="0 0 80 72" aria-hidden="true">
      <circle cx="25" cy="14" r="8" fill="var(--sage-icon)"/>
      <circle cx="55" cy="14" r="8" fill="var(--sage-icon)"/>
      <path d="M14 30 q11-8 22 0 v18 h-4 v20 h-14 v-20 h-4z" fill="var(--sage-icon)"/>
      <path d="M44 30 q11-8 22 0 v18 h-4 v20 h-14 v-20 h-4z" fill="var(--sage-icon)"/>
      <path d="M34 40 h12" stroke="var(--paper)" stroke-width="3"/>
    </svg>
    <h2 class="service-title">SOZIALE FÜRSORGE &amp;<br>DEMENZBEGLEITUNG</h2>
    <p class="service-text">Gesellschaft, Aktivierung<br>&amp; Entlastung für<br>Angehörige</p>
  </section>

  <section class="service service-home" style="left:778px">
    <svg viewBox="0 0 80 72" aria-hidden="true">
      <path d="M6 36 L40 6 L74 36" fill="none" stroke="var(--slate-icon)" stroke-width="6" stroke-linejoin="round"/>
      <path d="M16 32 V66 H64 V32 L40 12Z" fill="var(--slate-icon)"/>
      <rect x="33" y="44" width="14" height="22" fill="var(--paper)"/>
    </svg>
    <h2 class="service-title">HAUSWIRTSCHAFTLICHE<br>HILFE</h2>
    <p class="service-text">Sauberkeit, Wäsche<br>&amp; Mahlzeiten.</p>
  </section>

  <div class="photo photo-friends" role="img" aria-label="Foto: zwei Seniorinnen schauen lachend gemeinsam ein Fotoalbum an"></div>
  <div class="photo photo-groceries" role="img" aria-label="Foto: Betreuer übergibt einem älteren Herrn eine Einkaufstüte mit Gemüse"></div>
  <div class="photo photo-plants" role="img" aria-label="Foto: Seniorin pflegt Kräutertöpfe am Fenster"></div>

  <div class="legal-band">Wir sind für Sie da nach §43/b, §45a/b &amp; §53b SGB XI.</div>

  <p class="contact contact-line1"><span>Tel: 07531-918240</span><span>Email: info@sonnwerk-hilfe.de</span></p>
  <p class="contact contact-line2">Web: www.sonnwerk.de</p>
</div>
</body>
</html>
```